Brightvale services brochure

We need a new company brochure. The brochure will be formatted for PDF distribution but should be printable on "letter" size paper. 2 pages plus front and back cover. Color white and same blue as logo. Logo "O" should be used as design. Look at webpage for general info: www.brightvale-example.ca<br/><br/>Front cover: pic1, logo, design and "Your Cleaning is Our Business". <br/>Back cover" "O" design, logo and info from "contact" page<br/>Front cover inside: design and intro from web home page, also use stock pics of clean offices ect as placeholders for purchased pics.<br/>1st page: design and "Our Services", use info of "Cleanroom & GMP Services", "Janitorial Services" from services page.<br/>2nd page: design and "Special Services", info from "Carpet & Upholstery Services", "Window Cleaning Services", and list of "Other Services".<br/>Back cover inside : design and info from technology page, use stock pics for place holders.

Industry/Entity Type

Janitorial

Font styles to use
Sans Serif
Other font styles liked:
• Futura Book

Colors
0555a3

Requirements
Must have
• The logo "O" (target) should be part of the design. Design color same as logo.

```html
<!DOCTYPE html>
<html lang="en">
<head>
<meta charset="utf-8">
<title>Brightvale services brochure</title>
<link rel="stylesheet" href="https://fonts.googleapis.com/css2?family=Montserrat:wght@400;500;600;700;800&display=swap">
<style>
:root{
  --blue-deep:#0a4f95;
  --blue:#0555a3;
  --blue-bright:#1b83d3;
  --blue-pale:#d2e6f6;
  --grey-text:#6f7276;
  --ink:#34383d;
  --paper:#ffffff;
  --stage:#e3e4e6;
}
*{box-sizing:border-box;margin:0;padding:0}
html,body{width:1200px;height:2832px;overflow:hidden}
body{background:var(--stage);font-family:"Montserrat",sans-serif;color:var(--ink)}

.scene{height:944px;display:flex;align-items:center;justify-content:center}
.spread{display:flex;box-shadow:0 18px 40px rgba(0,0,0,.18)}
.page-slot{position:relative;overflow:hidden;background:var(--paper)}
.page-slot--single{width:600px;height:776px;box-shadow:0 18px 40px rgba(0,0,0,.18)}
.page-slot--half{width:500px;height:647px}
.page{position:absolute;left:0;top:0;width:600px;height:776px;overflow:hidden;background:var(--paper)}
.page-slot--half .page{transform:scale(.8334);transform-origin:0 0}
.art{position:absolute;left:0;top:0}

.wordmark{font-family:"Montserrat",sans-serif;font-weight:500;color:var(--blue-bright);letter-spacing:7px;text-transform:uppercase}

/* front cover */
.cover-front .wordmark{position:absolute;left:300px;top:64px;font-size:32px}
.cover-photo{position:absolute;left:140px;top:150px;width:360px;height:360px;border-radius:50%;
  background:linear-gradient(160deg,#eef3f6 0%,#c4d3dc 40%,#7f98a8 70%,#5f7b55 100%)}
.headline{position:absolute;left:172px;top:584px}
.headline__lead{font-weight:800;font-size:45px;color:var(--blue-bright);line-height:1;letter-spacing:.5px}
.headline__sub{font-weight:700;font-size:33px;color:var(--grey-text);line-height:1.2;letter-spacing:1px;margin-top:4px}
.headline__rule{width:110px;height:4px;background:var(--blue-bright);margin:6px 0 0 168px}

/* inside left */
.intro{position:absolute;left:40px;top:36px;width:520px}
.intro h2{font-size:22px;font-weight:800;color:var(--blue-bright);margin-bottom:8px}
.intro p{font-size:11.5px;line-height:1.45;color:var(--ink)}
.pill{position:absolute;left:40px;top:164px;background:#8a8d91;color:#fff;font-size:15px;font-weight:600;
  padding:6px 22px;border-radius:18px;letter-spacing:1px}
.services{position:absolute;left:36px;top:218px;width:530px;list-style:none}
.service{display:flex;gap:16px;margin-bottom:20px}
.service__icon{flex:0 0 50px;height:50px;border-radius:50%;background:#fff;border:3px solid var(--blue-pale)}
.service h3{font-size:16px;font-weight:700;color:#fff;letter-spacing:.5px;text-transform:uppercase}
.service p{font-size:10.5px;line-height:1.4;color:#dbe9f6;margin-top:3px}

/* inside right */
.screen{position:absolute;border-radius:6px;background:linear-gradient(135deg,#cfd6dc,#8b98a3)}
.screen--tablet{left:40px;top:34px;width:170px;height:110px}
.screen--report{left:320px;top:486px;width:240px;height:68px;background:linear-gradient(90deg,#f1f1f1,#dfe6ea)}
.qc{position:absolute;left:226px;top:40px;width:340px}
.qc h2,.feature h3{color:var(--blue-bright);font-weight:800;text-transform:uppercase}
.qc h2{font-size:17px;margin-bottom:6px}
.qc p,.feature p{font-size:10.5px;line-height:1.4}
.feature{position:absolute;width:240px;padding-left:40px}
.feature h3{font-size:13px;margin-bottom:3px}
.feature svg{position:absolute;left:0;top:0}
.feature--inspect{left:40px;top:170px}
.feature--schedule{left:40px;top:270px}
.feature--time{left:40px;top:370px;width:270px;padding-left:0}
.feature--order{left:320px;top:186px}
.feature--reports{left:320px;top:300px;width:250px}
.ticks{list-style:none;margin-top:6px}
.ticks li{font-size:10.5px;padding-left:20px;position:relative;margin-bottom:3px}
.ticks li svg{position:absolute;left:0;top:1px}
.band{position:absolute;left:0;bottom:0;width:600px;height:170px;background:var(--blue-deep)}
.band .wordmark{position:absolute;left:40px;top:66px;font-size:26px;color:#fff}
.band-photo{position:absolute;left:390px;top:10px;width:170px;height:170px;border-radius:50%;
  border:8px solid #fff;background:linear-gradient(150deg,#e9eef2,#9fb6c7 55%,#4b86b8)}

/* back cover */
.cover-back{background:var(--blue-deep)}
.contact{position:absolute;left:46px;top:530px;color:#fff}
.contact h2{font-size:22px;font-weight:700;letter-spacing:1px}
.contact__rule{width:40px;height:3px;background:#fff;margin:4px 0 16px}
.contact li{list-style:none;display:flex;align-items:center;gap:12px;font-size:15px;margin-bottom:9px}
.follow{position:absolute;left:340px;top:680px;color:#fff;font-weight:700;font-size:14px}
.cover-back .wordmark{position:absolute;left:340px;top:706px;font-size:24px;color:#fff}
</style>
</head>
<body>

<!-- front cover -->
<section class="scene">
  <div class="page-slot page-slot--single">
    <div class="page cover-front">
      <svg class="art" width="600" height="776" viewBox="0 0 600 776" aria-hidden="true">
        <circle cx="110" cy="760" r="86" fill="none" stroke="var(--blue-pale)" stroke-width="30"/>
        <circle cx="320" cy="330" r="194" fill="none" stroke="var(--blue-pale)" stroke-width="3"/>
        <circle cx="312" cy="336" r="204" fill="none" stroke="var(--blue-bright)" stroke-width="14" stroke-dasharray="820 1400" transform="rotate(40 312 336)"/>
      </svg>
      <p class="wordmark">Brightvale</p>
      <div class="cover-photo" role="img" aria-label="Photo of glass office towers seen from below"></div>
      <div class="headline">
        <p class="headline__lead">YOUR CLEANING</p>
        <p class="headline__sub">IS OUR BUSINESS</p>
        <div class="headline__rule"></div>
      </div>
    </div>
  </div>
</section>

<!-- inside spread -->
<section class="scene">
  <div class="spread">
    <div class="page-slot page-slot--half">
      <div class="page inside-left">
        <svg class="art" width="600" height="776" viewBox="0 0 600 776" aria-hidden="true">
          <defs><linearGradient id="panel" x1="0" y1="0" x2="0" y2="1"><stop offset="0" stop-color="#1b83d3"/><stop offset="1" stop-color="#0a4f95"/></linearGradient></defs>
          <path d="M0 200 Q300 150 600 120 L600 776 L0 776 Z" fill="url(#panel)"/>
        </svg>
        <div class="intro">
          <h2>YOUR CLEANING IS OUR BUSINESS!</h2>
          <p>Brightvale, a Janitorial Services Company in business since 1985, takes pride in providing complete cleaning services of the highest quality to all valued clients. We serve clients across the region and many areas across Canada.</p>
        </div>
        <p class="pill">OUR SERVICES</p>
        <ul class="services">
          <li class="service"><span class="service__icon"></span><div><h3>Janitorial Services</h3><p>Brightvale provides complete janitorial services for any type of facility and currently serves both public and private sector clients.</p></div></li>
          <li class="service"><span class="service__icon"></span><div><h3>Carpet &amp; Upholstery Services</h3><p>Brightvale provides a full carpet and upholstery cleaning service.</p></div></li>
          <li class="service"><span class="service__icon"></span><div><h3>Fire and Flood Restoration Services</h3><p>Brightvale can provide full fire and flood restoration services.</p></div></li>
          <li class="service"><span class="service__icon"></span><div><h3>Cleanroom &amp; GMP Services</h3><p>Brightvale is a leader in cleanroom and GMP services, with an impressive performance record.</p></div></li>
          <li class="service"><span class="service__icon"></span><div><h3>Window Cleaning Services</h3><p>Brightvale can tackle both high-rise and low-level window cleaning.</p></div></li>
          <li class="service"><span class="service__icon"></span><div><h3>Sanitation Supplies</h3><p>Brightvale supplies quality janitorial supplies. Contact us for a full list of supplies in stock.</p></div></li>
        </ul>
      </div>
    </div>
    <div class="page-slot page-slot--half">
      <div class="page inside-right">
        <div class="screen screen--tablet" role="img" aria-label="Photo of hands holding a tablet showing the online service system"></div>
        <div class="qc">
          <h2>Quality Control System</h2>
          <p>Brightvale supports a real time interactive system that monitors and manages customer satisfaction, giving customers the tools to control their services. Through the online web based system our customers have access and control of the following:</p>
        </div>
        <div class="feature feature--inspect">
          <svg width="30" height="30" viewBox="0 0 30 30" aria-hidden="true"><rect x="6" y="5" width="18" height="22" rx="2" fill="none" stroke="#8a8d91" stroke-width="2"/><rect x="11" y="2" width="8" height="5" rx="1" fill="#8a8d91"/><path d="M10 13h10M10 18h10M10 23h6" stroke="#8a8d91" stroke-width="2"/></svg>
          <h3>Inspections</h3>
          <p>Track trends to improve service. Perform detailed inspections. Track job performance. Correct deficiencies.</p>
        </div>
        <div class="feature feature--schedule">
          <svg width="30" height="30" viewBox="0 0 30 30" aria-hidden="true"><circle cx="15" cy="15" r="11" fill="none" stroke="#8a8d91" stroke-width="2"/><path d="M15 8v7l5 3" fill="none" stroke="#8a8d91" stroke-width="2"/></svg>
          <h3>Job Scheduling</h3>
          <p>Track compliance to contract specifications. Customize schedules to customer needs. Record daily and periodic services. Set automatic reminders.</p>
        </div>
        <div class="feature feature--time">
          <h3>Automated Time Keeping</h3>
          <p>Brightvale meets the increasing need for information accuracy and reliability with a computerised timekeeping system with realtime control of employees:</p>
          <ul class="ticks">
            <li><svg width="12" height="12" viewBox="0 0 12 12" aria-hidden="true"><circle cx="6" cy="6" r="5.5" fill="none" stroke="var(--blue-bright)"/><path d="M3 6l2 2 4-4" fill="none" stroke="var(--blue-bright)" stroke-width="1.5"/></svg>Realtime employee communications</li>
            <li><svg width="12" height="12" viewBox="0 0 12 12" aria-hidden="true"><circle cx="6" cy="6" r="5.5" fill="none" stroke="var(--blue-bright)"/><path d="M3 6l2 2 4-4" fill="none" stroke="var(--blue-bright)" stroke-width="1.5"/></svg>Realtime management of hours</li>
            <li><svg width="12" height="12" viewBox="0 0 12 12" aria-hidden="true"><circle cx="6" cy="6" r="5.5" fill="none" stroke="var(--blue-bright)"/><path d="M3 6l2 2 4-4" fill="none" stroke="var(--blue-bright)" stroke-width="1.5"/></svg>Realtime no show alerts</li>
            <li><svg width="12" height="12" viewBox="0 0 12 12" aria-hidden="true"><circle cx="6" cy="6" r="5.5" fill="none" stroke="var(--blue-bright)"/><path d="M3 6l2 2 4-4" fill="none" stroke="var(--blue-bright)" stroke-width="1.5"/></svg>Realtime on site attendance checks</li>
          </ul>
        </div>
        <div class="feature feature--order">
          <svg width="30" height="30" viewBox="0 0 30 30" aria-hidden="true"><rect x="4" y="6" width="20" height="20" fill="none" stroke="#8a8d91" stroke-width="2"/><path d="M12 19l2-5 12-12 3 3-12 12z" fill="#8a8d91"/></svg>
          <h3>Work Order Management</h3>
          <p>Instantly distribute work orders to those responsible. Automatically escalate work orders. Single point communications. Change or cancel work orders.</p>
        </div>
        <div class="feature feature--reports">
          <svg width="30" height="30" viewBox="0 0 30 30" aria-hidden="true"><path d="M7 3h11l6 6v18H7z" fill="#8a8d91"/><path d="M11 14h9M11 18h9M11 22h6" stroke="#fff" stroke-width="1.5"/></svg>
          <h3>Reports</h3>
          <p>Track compliance to contract specifications. Customize schedules to customer needs. Record daily and periodic services. Set automatic reminders.</p>
        </div>
        <div class="screen screen--report" role="img" aria-label="Screenshot of an online report dashboard"></div>
        <div class="band">
          <p class="wordmark">Brightvale</p>
          <div class="band-photo" role="img" aria-label="Photo of a gloved hand wiping a window sill"></div>
        </div>
      </div>
    </div>
  </div>
</section>

<!-- outside spread -->
<section class="scene">
  <div class="spread">
    <div class="page-slot page-slot--half">
      <div class="page cover-back">
        <svg class="art" width="600" height="776" viewBox="0 0 600 776" aria-hidden="true">
          <defs>
            <clipPath id="backPhoto"><circle cx="120" cy="120" r="340"/></clipPath>
            <linearGradient id="glass" x1="0" y1="0" x2="1" y2="1"><stop offset="0" stop-color="#2f78c4"/><stop offset="1" stop-color="#0d4c8f"/></linearGradient>
          </defs>
          <circle cx="120" cy="120" r="364" fill="none" stroke="#2b7fd0" stroke-width="6"/>
          <circle cx="120" cy="120" r="350" fill="none" stroke="#fff" stroke-width="10"/>
          <circle cx="400" cy="800" r="70" fill="none" stroke="#2f6eb0" stroke-width="24"/>
          <g role="img" aria-label="Photo of a glass office tower in blue tones">
            <rect x="0" y="0" width="600" height="776" fill="url(#glass)" clip-path="url(#backPhoto)"/>
          </g>
        </svg>
        <div class="contact">
          <h2>CONTACT US</h2>
          <div class="contact__rule"></div>
          <ul>
            <li><svg width="18" height="18" viewBox="0 0 18 18" aria-hidden="true"><circle cx="9" cy="9" r="8.5" fill="#fff"/><path d="M6 5l2 2-1 1.5a6 6 0 0 0 2.5 2.5L11 10l2 2-1.5 1.5C8 13 5 10 4.5 6.5z" fill="var(--blue-deep)"/></svg>1 (800) 555-0142</li>
            <li><svg width="18" height="18" viewBox="0 0 18 18" aria-hidden="true"><circle cx="9" cy="9" r="8.5" fill="#fff"/><rect x="4.5" y="6" width="9" height="6" fill="none" stroke="var(--blue-deep)" stroke-width="1.2"/><path d="M4.5 6l4.5 3.5L13.5 6" fill="none" stroke="var(--blue-deep)" stroke-width="1.2"/></svg>info@brightvale-example.ca</li>
            <li><svg width="18" height="18" viewBox="0 0 18 18" aria-hidden="true"><circle cx="9" cy="9" r="8.5" fill="#fff"/><circle cx="9" cy="9" r="5" fill="none" stroke="var(--blue-deep)" stroke-width="1.2"/><path d="M9 6.5V9l2 1" fill="none" stroke="var(--blue-deep)" stroke-width="1.2"/></svg>Monday - Friday 9am-5pm</li>
          </ul>
        </div>
        <p class="follow">Follow us online</p>
        <p class="wordmark">Brightvale</p>
      </div>
    </div>
    <div class="page-slot page-slot--half">
      <div class="page cover-front">
        <svg class="art" width="600" height="776" viewBox="0 0 600 776" aria-hidden="true">
          <circle cx="110" cy="760" r="86" fill="none" stroke="var(--blue-pale)" stroke-width="30"/>
          <circle cx="320" cy="330" r="194" fill="none" stroke="var(--blue-pale)" stroke-width="3"/>
          <circle cx="312" cy="336" r="204" fill="none" stroke="var(--blue-bright)" stroke-width="14" stroke-dasharray="820 1400" transform="rotate(40 312 336)"/>
        </svg>
        <p class="wordmark">Brightvale</p>
        <div class="cover-photo" role="img" aria-label="Photo of glass office buildings with trees below"></div>
        <div class="headline">
          <p class="headline__lead">YOUR CLEANING</p>
          <p class="headline__sub">IS OUR BUSINESS</p>
          <div class="headline__rule"></div>
        </div>
      </div>
    </div>
  </div>
</section>

</body>
</html>
```